New website for a commercial real estate consulting company

What we’re looking for in a new web site:
• Desktop and mobile friendly
• Clear navigation
• Strong graphics
• Professional appearance
• The ability to update it ourselves
• Site is for information purposes only – no transactions required
• Traffic counts – number of visits per page?
• A firm quote on costs to develop and launch
• SSL
Attached is a copy of the revised text we propose to use, including our new logo. (The pagination can be different than as shown.)
Our current website address is www.tamblinvaleadvisory.ca

```html
<!DOCTYPE html>
<html lang="en">
<head>
<meta charset="utf-8">
<title>Tamblin Vale Advisory</title>
<link rel="stylesheet" href="https://fonts.googleapis.com/css2?family=Roboto:ital,wght@0,300;0,400;0,500;0,700;1,400&display=swap">
<style>
  :root {
    --brand-blue: #283a8e;
    --brand-blue-text: #2b3d94;
    --panel-grey: #f0f0f0;
    --ink: #1c1c1c;
    --white: #ffffff;
    --footer-text: #c9cfe6;
  }
  * { box-sizing: border-box; margin: 0; padding: 0; }
  html, body { width: 1200px; height: 2250px; overflow: hidden; }
  body {
    position: relative;
    background: var(--white);
    font-family: 'Roboto', Arial, sans-serif;
    color: var(--ink);
  }
  .sidebar {
    position: absolute; left: 0; top: 0; width: 250px; height: 660px;
    background: var(--panel-grey);
  }
  .brand {
    position: absolute; left: 0; top: 40px; width: 250px;
    text-align: center; color: var(--brand-blue);
  }
  .brand-mark {
    display: block; width: 56px; height: 56px; margin: 0 auto 14px;
    background: var(--brand-blue);
  }
  .brand-name {
    font-size: 21px; font-weight: 500; letter-spacing: 1px; text-transform: uppercase; line-height: 1.2;
  }
  .main-nav { position: absolute; left: 23px; top: 234px; list-style: none; }
  .main-nav li { font-size: 25px; line-height: 47.5px; color: var(--ink); }
  .sidebar-phone {
    position: absolute; left: 23px; top: 606px;
    font-size: 25px; font-weight: 700; color: var(--brand-blue-text);
  }
  .hero {
    position: absolute; left: 250px; top: 0; width: 950px; height: 435px;
    background: linear-gradient(135deg, #3a3d42 0%, #6e7277 45%, #8d9094 70%, #5a5d61 100%);
  }
  .hero-title {
    position: absolute; left: 0; top: 158px; width: 950px;
    text-align: center; color: var(--white);
    font-size: 55px; font-weight: 400; line-height: 68px; letter-spacing: 1px;
  }
  .tagline-band {
    position: absolute; left: 250px; top: 435px; width: 950px; height: 70px;
    background: var(--brand-blue); color: var(--white);
    font-size: 31px; line-height: 70px; text-align: center;
  }
  .photo { position: absolute; }
  .photo-meeting {
    left: 250px; top: 505px; width: 476px; height: 485px;
    background: linear-gradient(160deg, #8a6f55 0%, #b39677 40%, #d2c3b0 70%, #6a5a4d 100%);
  }
  .photo-handshake {
    left: 726px; top: 990px; width: 474px; height: 513px;
    background: linear-gradient(150deg, #5d6f85 0%, #aab3bd 45%, #d7d1c9 70%, #7d6b5c 100%);
  }
  .copy { position: absolute; font-size: 22px; line-height: 27.5px; color: var(--ink); font-weight: 300; }
  .copy p + p { margin-top: 27px; }
  .copy .accent { color: var(--brand-blue-text); font-weight: 400; }
  .copy-intro { left: 771px; top: 546px; width: 400px; }
  .copy-history { left: 288px; top: 1033px; width: 410px; }
  .btn-contact {
    position: absolute; width: 186px; height: 43px;
    background: var(--brand-blue); color: var(--white);
    font-size: 26px; font-weight: 500; line-height: 43px; text-align: center;
  }
  .btn-intro { left: 771px; top: 901px; }
  .btn-clients { left: 621px; top: 1878px; }
  .clients {
    position: absolute; left: 250px; top: 1503px; width: 950px; height: 465px;
    background: var(--panel-grey);
  }
  .clients-heading {
    position: absolute; left: 0; top: 40px; width: 950px; text-align: center;
    font-size: 32px; font-weight: 700; color: var(--brand-blue-text);
  }
  .client-list { position: absolute; top: 143px; list-style: none; font-size: 22px; line-height: 29px; font-weight: 300; }
  .client-list-left { left: 46px; width: 330px; }
  .client-list-right { left: 510px; width: 330px; }
  .client-list li { position: relative; padding-left: 45px; }
  .client-list .tick { position: absolute; left: 0; top: 2px; width: 32px; height: 22px; }
  .quote-band {
    position: absolute; left: 250px; top: 1968px; width: 950px; height: 72px;
    background: var(--brand-blue); color: var(--white);
    font-size: 28px; font-style: italic; line-height: 72px; text-align: center;
  }
  .contact-note {
    position: absolute; left: 300px; top: 2069px; width: 850px; text-align: center;
    font-size: 24.5px; line-height: 30px; color: var(--brand-blue-text);
  }
  .site-footer {
    position: absolute; left: 250px; top: 2187px; width: 950px; height: 63px;
    background: var(--brand-blue); color: var(--footer-text);
    font-size: 21px; font-weight: 300; line-height: 63px; text-align: center;
  }
  .site-footer span + span { margin-left: 52px; }
</style>
</head>
<body>
  <svg width="0" height="0" style="position:absolute">
    <symbol id="icon-tick" viewBox="0 0 32 22">
      <path d="M3 11 L12 19 L29 3" fill="none" stroke="#283a8e" stroke-width="5" stroke-linecap="round" stroke-linejoin="round"/>
    </symbol>
  </svg>

  <aside class="sidebar">
    <div class="brand">
      <span class="brand-mark"></span>
      <div class="brand-name">Tamblin Vale<br>Advisory</div>
    </div>
    <ul class="main-nav">
      <li>Home</li>
      <li>Who Are We</li>
      <li>What We Do</li>
      <li>Contact Us</li>
      <li>Events calendar</li>
    </ul>
    <div class="sidebar-phone">905-555-0186</div>
  </aside>

  <header class="hero" role="img" aria-label="Photo of a person holding a smartphone above a desk with a tablet and coffee">
    <h1 class="hero-title">TAMBLIN VALE<br>ADVISORY</h1>
  </header>

  <div class="tagline-band">Expert | Experienced | Cost Effective</div>

  <div class="photo photo-meeting" role="img" aria-label="Overhead photo of a team meeting around a wooden table with laptops and documents"></div>

  <section class="copy copy-intro">
    <p>Tamblin Vale Advisory is an independent consulting firm offering practical, hands-on assistance to the commercial real estate and commercial mortgage lending industries. We specialize in financial analysis, underwriting and financial due diligence.</p>
    <p class="accent">Working with us, you get top notch help when you need it – and only when you need it – one project at a time.</p>
  </section>
  <div class="btn-contact btn-intro">CONTACT</div>

  <section class="copy copy-history">
    <p>Tamblin Vale Advisory has been providing expert, experienced and cost-effective service to the commercial real estate and commercial mortgage industries since 2001. We have worked on projects across Canada and the United States, and in every major property type.</p>
    <p>The foundation of our success has been our commitment to exceeding our clients’ expectations, both in quality and in timeliness. We strive to go above and beyond on every assignment.</p>
  </section>

  <div class="photo photo-handshake" role="img" aria-label="Photo of two business people shaking hands over a desk with a laptop showing growth charts"></div>

  <section class="clients">
    <h2 class="clients-heading">OUR CLIENTS INCLUDE:</h2>
    <ul class="client-list client-list-left">
      <li><svg class="tick"><use href="#icon-tick"/></svg>Chartered banks</li>
      <li><svg class="tick"><use href="#icon-tick"/></svg>Mortgage bankers</li>
      <li><svg class="tick"><use href="#icon-tick"/></svg>Public REITs &amp; REOCs</li>
      <li><svg class="tick"><use href="#icon-tick"/></svg>Private equity firms</li>
      <li><svg class="tick"><use href="#icon-tick"/></svg>Family-owned real estate investment companies</li>
    </ul>
    <ul class="client-list client-list-right">
      <li><svg class="tick"><use href="#icon-tick"/></svg>Life insurance companies</li>
      <li><svg class="tick"><use href="#icon-tick"/></svg>Pension funds</li>
      <li><svg class="tick"><use href="#icon-tick"/></svg>Non-bank lenders</li>
      <li><svg class="tick"><use href="#icon-tick"/></svg>Brokerage firms</li>
    </ul>
  </section>
  <div class="btn-contact btn-clients">CONTACT</div>

  <div class="quote-band">“Reputation is the currency of the 21st century”</div>

  <p class="contact-note">For more information please call us at <strong>905-555-0186</strong>, email Maren Holloway at <strong>maren.holloway@tamblinvaleadvisory.ca</strong>, or fill out our form.</p>

  <footer class="site-footer">
    <span>T. 905-555-0186</span><span>E. maren.holloway@tamblinvaleadvisory.ca</span>
  </footer>
</body>
</html>
```